Speaker Overview Package

WHAT I NEED:
A professional speaker package INSPIRED BY Corinne Del Hastley example found in the attached url or by following this link: https://files.pavlorex.net/share/7kQwZp2LmXvR9tYb4NcJ8dHs/view?mode=open
Same page types and structure, but with YOUR original creative design using QR7 Lumen branding: www.QR7Lumen.com
USE ATTACHED PDF FOR:
Page structure and content sections (what pages to include)
Professional quality level to match
Type of information on each page
Overall organization and flow
YOUR ORIGINAL DESIGN SHOULD INCLUDE:
Same page types (bio, topics, pricing, testimonials, etc.)
QR7 Lumen (www.QR7Lumen.com) branding from qr7lumen.com (colors, fonts, style)
Your own creative layout and design approach
Professional, corporate-friendly aesthetic
REQUIRED PAGE TYPES (like the example):
Cover page
Speaker bio/credentials
Methodology/approach page
Speaking topics (3-4 keynotes)
Testimonials
Event types offered
Pricing/packages
Workshop pricing
Client logos
Press/media mentions
Contact/booking
DELIVERABLES:
Original creative design (not copied from example)
QR7 branding from qr7lumen.com
Print-ready PDF (300 DPI) + source files
8.5" x 11" format
Professional quality matching reference
SUBMIT FOR ENTRY:
Cover page concept
2-3 sample interior pages showing your design style
CRITICAL:
Use the example for STRUCTURE and CONTENT TYPES only. I want YOUR creative design using QR7 branding. NO copying Corinne's graphics/layout. NO AI-generated designs.

```html
<!DOCTYPE html>
<html lang="en">
<head>
<meta charset="utf-8">
<title>QR7 Lumen — Rafael Quintero Speaker Overview Package</title>
<link href="https://fonts.googleapis.com/css2?family=Playfair+Display:wght@600;700;800&family=Inter:wght@400;500;600;700&display=swap" rel="stylesheet">
<style>
:root{
  --ink:#0c0c0c;
  --night:#080808;
  --panel:#161616;
  --edge:#2c2c2c;
  --red:#e1232b;
  --white:#ffffff;
  --paper:#ffffff;
  --mist:#f1f1f1;
  --grey:#8d8d8d;
  --soft:#bdbdbd;
  --rule:#d9d9d9;
}
*{box-sizing:border-box;margin:0;padding:0}
html,body{width:1200px;height:2872px;overflow:hidden;background:var(--white);font-family:"Inter",Arial,sans-serif;color:var(--ink)}
.board{width:1200px;height:2872px;display:grid;grid-template-columns:564px 564px;grid-auto-rows:362px;column-gap:24px;row-gap:40px;padding:49px 24px}
.spread{display:flex;gap:4px;box-shadow:0 2px 10px rgba(0,0,0,.18)}
.page{width:280px;height:362px;position:relative;overflow:hidden;padding:22px 18px}
.dark{background:var(--night);color:var(--white)}
.light{background:var(--paper);color:var(--ink)}
.cover{width:564px;height:362px;position:relative;overflow:hidden;background:var(--night);color:var(--white)}

.title{font-family:"Playfair Display",Georgia,serif;font-weight:800;font-size:19px;line-height:1.08;letter-spacing:-.2px}
.title.sm{font-size:14px}
.title .accent{color:var(--red)}
.kicker{font-size:5.5px;font-weight:700;letter-spacing:.9px;text-transform:uppercase;color:var(--red)}
.body{font-size:5px;line-height:1.55;color:#6a6a6a}
.dark .body{color:var(--soft)}
.label{font-size:6px;font-weight:700;line-height:1.3}
.rule{height:2px;width:34px;background:var(--red);margin:6px 0}
.mark{font-family:"Inter",Arial,sans-serif;font-weight:700;color:var(--white);letter-spacing:.5px}
.mark.ink{color:var(--ink)}
.photo{border-radius:3px}
.folio{position:absolute;bottom:9px;right:14px;font-size:5px;color:var(--grey)}

.card{border:1px solid var(--rule);border-radius:4px;padding:7px}
.dark .card{border-color:var(--edge);background:var(--panel)}
.card .label{margin-bottom:3px}
.pill{border-radius:999px;padding:7px 10px;display:flex;align-items:center;gap:8px}
.pill.black{background:var(--ink);color:var(--white)}
.pill.outline{border:1px solid var(--edge);background:var(--panel)}
.dot{width:16px;height:16px;border-radius:50%;flex:none}
.tick{width:7px;height:7px;flex:none}
.row{display:flex;gap:6px;align-items:flex-start}
.list{display:flex;flex-direction:column;gap:6px}
.grid2{display:grid;grid-template-columns:1fr 1fr;gap:6px}
.bar{background:var(--ink);color:var(--white);border-radius:999px;padding:5px 10px;font-size:6px;font-weight:700;letter-spacing:.8px;text-transform:uppercase;display:inline-flex;align-items:center;gap:6px}
.bar::before{content:"";width:6px;height:6px;border-radius:50%;background:var(--red)}
.price-row{display:flex;justify-content:space-between;align-items:center;border-bottom:1px solid var(--rule);padding:5px 0}
.dark .price-row{border-color:var(--edge)}
.price{font-family:"Playfair Display",Georgia,serif;font-weight:700;font-size:8px;color:var(--red)}
.quote{font-family:"Playfair Display",Georgia,serif;font-size:22px;color:var(--red);line-height:.6}
.logo-tile{height:26px;border-radius:3px;background:var(--mist)}
</style>
</head>
<body>
<main class="board">

  <!-- Cover -->
  <section class="spread">
    <div class="cover">
      <div class="photo" role="img" aria-label="Portrait of the speaker in a dark suit behind a large monogram" style="position:absolute;left:0;top:0;width:300px;height:362px;background:radial-gradient(ellipse at 55% 45%,#4a4a4a 0%,#1c1c1c 45%,#060606 80%);border-radius:0"></div>
      <div class="mark" style="position:absolute;left:40px;top:120px;font-size:92px;color:#2e2e2e;letter-spacing:-2px">QR7</div>
      <div style="position:absolute;left:300px;top:112px;width:240px">
        <div class="kicker">Keynote Speaker · Author · Coach</div>
        <div class="title" style="font-size:34px;margin-top:6px">Rafael<br>Quintero</div>
        <div class="rule" style="width:60px"></div>
        <div style="font-size:7px;line-height:1.5;color:var(--soft)">Building Resilient, <span style="color:var(--red);font-weight:700">Disciplined</span> &amp; High-Performing Organizations</div>
      </div>
      <div style="position:absolute;left:22px;bottom:20px;display:flex;align-items:center;gap:5px">
        <span class="mark" style="font-size:13px">QR7</span><span style="font-size:5px;color:var(--grey);letter-spacing:1px">LUMEN</span>
      </div>
    </div>
  </section>

  <!-- Bio + Advantage -->
  <section class="spread">
    <div class="page light">
      <div class="title">Rafael Quintero</div>
      <div class="kicker" style="margin-top:4px">Growth Strategist · Keynote Speaker · Founder</div>
      <div class="rule"></div>
      <div class="row" style="margin-top:6px">
        <div class="photo" role="img" aria-label="Portrait of the speaker on stage" style="width:118px;height:130px;flex:none;background:linear-gradient(160deg,#5a5a5a,#151515)"></div>
        <div class="body">Rafael has spent two decades helping leaders turn pressure into progress. He built and scaled three companies, led sales teams across four markets and now coaches executives on discipline, focus and growth.</div>
      </div>
      <p class="body" style="margin-top:10px">His keynotes blend lived experience with a clear framework audiences can apply the next morning. Clients value his direct style, practical tools and the energy he brings to every room, from small leadership retreats to national conferences.</p>
      <p class="body" style="margin-top:6px">He is the creator of the QR7 Methodology, a three-level system for personal, team and business growth used by firms in finance, retail, tech and health.</p>
      <div style="position:absolute;left:18px;right:18px;bottom:22px;background:var(--ink);color:var(--white);border-radius:4px;padding:8px 10px;font-size:5.5px;line-height:1.5">
        <b style="color:var(--red)">20+ years</b> leading teams · <b style="color:var(--red)">500+</b> events · <b style="color:var(--red)">3</b> companies built
      </div>
    </div>
    <div class="page light">
      <div class="title">The <span class="accent">QR7</span> Advantage</div>
      <div class="kicker" style="margin-top:4px">Why leaders choose Rafael</div>
      <div class="rule"></div>
      <div style="position:relative;margin-top:14px">
        <div class="grid2" style="gap:8px">
          <div class="card" style="height:92px"><div class="label">Proven Results</div><div class="body">Tools tested in real companies, not theory from a desk.</div></div>
          <div class="card" style="height:92px;text-align:right"><div class="label">Clear Framework</div><div class="body">Three levels of growth your people can repeat.</div></div>
          <div class="card" style="height:92px"><div class="label">Real Energy</div><div class="body">Sessions that move rooms and keep momentum high.</div></div>
          <div class="card" style="height:92px;text-align:right"><div class="label">Lasting Change</div><div class="body">Follow-up plans that turn one day into a habit.</div></div>
        </div>
        <div class="photo" role="img" aria-label="Speaker portrait framed in a dark square" style="position:absolute;left:50%;top:50%;width:70px;height:70px;margin:-35px 0 0 -35px;background:linear-gradient(150deg,#3d3d3d,#0a0a0a);border:3px solid var(--white)"></div>
      </div>
      <p class="body" style="margin-top:14px">Each engagement is shaped around your goals, your audience and the change you want to see after the event.</p>
      <span class="folio">03</span>
    </div>
  </section>

  <!-- Powerful Presentations + Resources -->
  <section class="spread">
    <div class="page dark">
      <div class="title">Powerful Presentations for Thriving Organizations</div>
      <div class="rule"></div>
      <div class="photo" role="img" aria-label="Speaker presenting to a large audience" style="height:70px;margin-top:8px;background:linear-gradient(120deg,#2b2b2b,#0d0d0d 70%)"></div>
      <div class="list" style="margin-top:12px">
        <div class="pill outline"><span class="dot" role="img" aria-label="Client headshot" style="background:#444"></span><div><div class="body">“Rafael gave our team a shared language for growth. Sales rose in the first quarter.”</div><div class="label" style="font-size:5px;margin-top:2px;color:var(--red)">Regional Director, Retail Group</div></div></div>
        <div class="pill outline"><span class="dot" role="img" aria-label="Client headshot" style="background:#444"></span><div><div class="body">“The best keynote of our conference. People were still talking about it weeks later.”</div><div class="label" style="font-size:5px;margin-top:2px;color:var(--red)">Event Chair, Finance Summit</div></div></div>
      </div>
    </div>
    <div class="page light">
      <div class="title">Resources &amp; Upcoming Book</div>
      <div class="rule"></div>
      <div class="row" style="margin-top:10px">
        <div role="img" aria-label="Book cover in black and red" style="width:80px;height:112px;flex:none;background:linear-gradient(160deg,#222,#000);border-radius:2px;box-shadow:3px 3px 0 var(--red)"></div>
        <div>
          <div class="label">The Resilient Climb</div>
          <div class="kicker" style="margin:3px 0 5px">Coming next spring</div>
          <div class="body">A field guide to discipline, grit and steady growth for leaders who want results that last beyond a good quarter.</div>
        </div>
      </div>
      <div class="list" style="margin-top:14px">
        <div class="row"><svg class="tick" viewBox="0 0 8 8"><path d="M1 4l2 2 4-4" stroke="#e1232b" stroke-width="1.4" fill="none"/></svg><div class="body">Weekly growth notes for leaders and teams</div></div>
        <div class="row"><svg class="tick" viewBox="0 0 8 8"><path d="M1 4l2 2 4-4" stroke="#e1232b" stroke-width="1.4" fill="none"/></svg><div class="body">Workbooks that pair with each keynote</div></div>
        <div class="row"><svg class="tick" viewBox="0 0 8 8"><path d="M1 4l2 2 4-4" stroke="#e1232b" stroke-width="1.4" fill="none"/></svg><div class="body">Video lessons on the QR7 Methodology</div></div>
      </div>
      <span class="folio">05</span>
    </div>
  </section>

  <!-- Event Types -->
  <section class="spread">
    <div class="page light">
      <div class="title">Event Types</div>
      <div class="rule"></div>
      <div class="list" style="margin-top:10px;gap:9px">
        <div class="card"><div class="label">Keynote Presentations</div><div class="body">High-energy talks of 45 to 90 minutes for conferences and kickoffs.</div></div>
        <div class="card"><div class="label">In-Person Keynotes &amp; Workshops</div><div class="body">Half-day or full-day sessions with hands-on exercises for teams.</div></div>
        <div class="card"><div class="label">Virtual Keynotes &amp; Training</div><div class="body">Live online sessions built for remote and hybrid audiences.</div></div>
        <div class="card"><div class="label">Leadership Retreats</div><div class="body">Small-group programs that align leaders on goals and habits.</div></div>
      </div>
      <span class="folio">06</span>
    </div>
    <div class="page light">
      <div class="card" style="background:var(--mist);border:none"><div class="label">Additional Engagement Types</div>
        <div class="grid2" style="margin-top:4px"><div class="body">· Panel moderation</div><div class="body">· Fireside chats</div><div class="body">· Sales kickoffs</div><div class="body">· Executive coaching</div></div>
      </div>
      <div class="row" style="margin-top:18px;align-items:center">
        <div class="photo" role="img" aria-label="Speaker standing with arms crossed" style="width:110px;height:150px;flex:none;background:linear-gradient(170deg,#6a6a6a,#1a1a1a)"></div>
        <div class="title sm">Bring the <span class="accent">Proven</span> Methodology to Your Company</div>
      </div>
      <p class="body" style="margin-top:12px">Every program is tailored after a short discovery call so your event speaks to your people, your market and your goals.</p>
      <span class="folio">07</span>
    </div>
  </section>

  <!-- Core Topics + Methodology -->
  <section class="spread">
    <div class="page light">
      <div class="title">Core Topics</div>
      <div class="rule"></div>
      <div class="list" style="margin-top:8px;gap:8px">
        <div class="card"><div class="kicker">01</div><div class="label">The QR7 Methodology</div><div class="body">Three levels of growth for people, teams and business.</div></div>
        <div class="card"><div class="kicker">02</div><div class="label">Build Your Business</div><div class="body">Growth strategies that scale without losing focus.</div></div>
        <div class="card"><div class="kicker">03</div><div class="label">The Competitive Edge</div><div class="body">Resilience, discipline and peak performance.</div></div>
        <div class="card"><div class="kicker">04</div><div class="label">Sales Mastery</div><div class="body">Winning long-term relationships in any market.</div></div>
      </div>
      <span class="folio">08</span>
    </div>
    <div class="page dark">
      <div class="title">The <span class="accent">QR7</span> Methodology: Master the Three Levels of Business Growth</div>
      <div class="rule"></div>
      <p class="body">A simple system leaders use to grow themselves, their teams and their companies at the same time.</p>
      <div class="list" style="margin-top:10px;gap:7px">
        <div class="card"><div class="label"><span style="color:var(--red)">Level 1</span> · Personal Growth</div><div class="body">Habits, mindset and daily discipline.</div></div>
        <div class="card"><div class="label"><span style="color:var(--red)">Level 2</span> · Team Growth</div><div class="body">Trust, clear roles and shared goals.</div></div>
        <div class="card"><div class="label"><span style="color:var(--red)">Level 3</span> · Business Growth</div><div class="body">Systems, sales and steady scale.</div></div>
      </div>
      <div class="row" style="margin-top:10px"><span class="quote">“</span><div class="body">Attendees leave with a one-page plan for each level.</div></div>
    </div>
  </section>

  <!-- Build Your Business -->
  <section class="spread">
    <div class="page dark">
      <div class="title sm"><span class="accent">Build</span> Your Business: Implementing Exponential Growth Strategies</div>
      <div class="rule"></div>
      <div class="photo" role="img" aria-label="Speaker gesturing during a talk" style="height:92px;margin-top:6px;background:linear-gradient(135deg,#343434,#0b0b0b)"></div>
      <div class="list" style="margin-top:10px">
        <div class="card"><div class="label">Key Takeaways</div><div class="body">Find the few moves that drive most of your growth and focus your team on them.</div></div>
        <div class="card"><div class="label">Ideal For</div><div class="body">Owners, founders and leadership teams ready to scale.</div></div>
      </div>
    </div>
    <div class="page dark">
      <div class="kicker">What your audience gains</div>
      <div class="list" style="margin-top:10px;gap:9px">
        <div class="row"><span class="quote">1</span><div class="body">A clear growth map with three priority moves for the next quarter.</div></div>
        <div class="row"><span class="quote">2</span><div class="body">Ways to remove the bottlenecks that slow good teams down.</div></div>
        <div class="row"><span class="quote">3</span><div class="body">Simple scorecards that keep every leader on the same page.</div></div>
      </div>
      <div class="pill outline" style="margin-top:18px"><span class="dot" role="img" aria-label="Client headshot" style="background:#444"></span><div class="body">“Practical, sharp and motivating. Our leaders put it to work the same week.”</div></div>
      <div class="pill outline" style="margin-top:8px"><span class="dot" role="img" aria-label="Client headshot" style="background:#444"></span><div class="body">“Rafael speaks from experience. That is why people listen.”</div></div>
    </div>
  </section>

  <!-- Competitive Edge -->
  <section class="spread">
    <div class="page dark">
      <div class="title sm">The <span class="accent">Competitive Edge</span>: Building Resilience, Discipline &amp; Peak Performance</div>
      <div class="rule"></div>
      <div class="photo" role="img" aria-label="Speaker on stage under spotlight" style="height:100px;margin-top:6px;background:radial-gradient(circle at 60% 40%,#555,#0a0a0a 70%)"></div>
      <p class="body" style="margin-top:10px">How top performers stay steady under pressure, keep promises to themselves and bounce back faster after setbacks.</p>
      <div class="grid2" style="margin-top:10px">
        <div class="card"><div class="label">Resilience</div><div class="body">Recover and refocus.</div></div>
        <div class="card"><div class="label">Discipline</div><div class="body">Small wins daily.</div></div>
      </div>
    </div>
    <div class="page dark">
      <div class="row" style="margin-top:6px"><span class="quote">“</span><div class="body" style="font-size:6px">Rafael delivered exactly what our people needed after a hard year. The room was electric.</div></div>
      <div class="kicker" style="margin:4px 0 0 16px">VP People, Health Network</div>
      <div class="row" style="margin-top:16px"><span class="quote">“</span><div class="body" style="font-size:6px">Clear, honest and full of tools. We booked him again for our next kickoff.</div></div>
      <div class="kicker" style="margin:4px 0 0 16px">CEO, Tech Services Firm</div>
      <div class="row" style="margin-top:16px"><span class="quote">“</span><div class="body" style="font-size:6px">He met with our leaders beforehand and tailored every story. It showed.</div></div>
      <div class="kicker" style="margin:4px 0 0 16px">Event Lead, Banking Forum</div>
    </div>
  </section>

  <!-- Sales Mastery -->
  <section class="spread">
    <div class="page dark">
      <div class="title sm">Sales Mastery in Any Market: <span class="accent">Proven Lessons</span> for Winning Long-Term Relationships</div>
      <div class="rule"></div>
      <div class="row" style="margin-top:8px">
        <div class="photo" role="img" aria-label="Speaker seated in a studio" style="width:100px;height:130px;flex:none;background:linear-gradient(160deg,#7a2a2a,#1a0a0a 60%,#0a0a0a)"></div>
        <div class="list">
          <div class="card"><div class="label">Trust First</div><div class="body">Earn the second sale before the first.</div></div>
          <div class="card"><div class="label">Ask Better</div><div class="body">Questions that open real needs.</div></div>
        </div>
      </div>
    </div>
    <div class="page dark">
      <div class="kicker">Program outcomes</div>
      <div class="list" style="margin-top:10px">
        <div class="card"><div class="label">Higher close rates</div><div class="body">A repeatable process every rep can follow.</div></div>
        <div class="card"><div class="label">Longer client life</div><div class="body">Service habits that keep buyers coming back.</div></div>
        <div class="card"><div class="label">Confident teams</div><div class="body">Scripts and role play that build real skill.</div></div>
      </div>
      <div class="pill outline" style="margin-top:14px"><span class="dot" role="img" aria-label="Client headshot" style="background:#444"></span><div class="body">“Our sales team finally works from one playbook.”</div></div>
    </div>
  </section>

  <!-- Keynote Pricing -->
  <section class="spread">
    <div class="page dark">
      <div class="kicker">Signature programs</div>
      <div class="grid2" style="margin-top:10px">
        <div class="card" style="height:72px"><div class="label">Keynote</div><div class="body">45–90 minute talk with live Q&amp;A.</div></div>
        <div class="card" style="height:72px"><div class="label">Workshop</div><div class="body">Half or full day, hands-on tools.</div></div>
        <div class="card" style="height:72px"><div class="label">Virtual</div><div class="body">Live online session for any size.</div></div>
        <div class="card" style="height:72px"><div class="label">Coaching</div><div class="body">One-to-one executive program.</div></div>
      </div>
      <div class="row" style="margin-top:14px"><span class="quote">“</span><div class="body">Every engagement starts with a discovery call to shape the message around your goals.</div></div>
    </div>
    <div class="page light">
      <div class="title">Keynote Pricing</div>
      <div class="rule"></div>
      <div class="bar" style="margin-top:6px">In-Person Keynote</div>
      <div style="margin-top:6px">
        <div class="price-row"><span class="label">Standard Keynote</span><span class="price">$15,000</span></div>
        <div class="price-row"><span class="label">Keynote + Breakout</span><span class="price">$20,000</span></div>
        <div class="price-row"><span class="label">Keynote + Book Bundle</span><span class="price">$24,000</span></div>
        <div class="price-row"><span class="label">Full Event Day</span><span class="price">$30,000</span></div>
      </div>
      <p class="body" style="margin-top:10px">Travel billed at cost. Custom content and pre-event calls included with every booking.</p>
      <span class="folio">15</span>
    </div>
  </section>

  <!-- Virtual / Additional options -->
  <section class="spread">
    <div class="page dark">
      <div class="bar" style="background:var(--white);color:var(--ink)">Virtual Keynotes</div>
      <div style="margin-top:8px">
        <div class="price-row"><span class="label">Live Virtual Keynote</span><span class="price">$8,000</span></div>
        <div class="price-row"><span class="label">Virtual + Q&amp;A Session</span><span class="price">$10,000</span></div>
        <div class="price-row"><span class="label">Virtual Series (3)</span><span class="price">$22,000</span></div>
      </div>
      <div class="photo" role="img" aria-label="Speaker presenting on a video call" style="height:92px;margin-top:14px;background:linear-gradient(180deg,#2a2a2a,#f1f1f1)"></div>
    </div>
    <div class="page dark">
      <div class="bar" style="background:var(--white);color:var(--ink)">Additional Options</div>
      <div style="margin-top:8px">
        <div class="price-row"><span class="label">Pre-Event Leader Call</span><span class="price">Included</span></div>
        <div class="price-row"><span class="label">Recorded Session Rights</span><span class="price">$3,500</span></div>
        <div class="price-row"><span class="label">Signed Book Bundle</span><span class="price">$2,000</span></div>
        <div class="price-row"><span class="label">Follow-Up Webinar</span><span class="price">$4,000</span></div>
      </div>
      <div class="card" style="margin-top:14px"><div class="label">Bundle &amp; Save</div><div class="body">Book two or more programs in one year and receive a reduced fee on each.</div></div>
    </div>
  </section>

  <!-- Workshop Pricing -->
  <section class="spread">
    <div class="page light">
      <div class="title">Workshop &amp; <br>Training Pricing</div>
      <div class="kicker" style="margin-top:4px">Hands-on learning for teams</div>
      <div class="rule"></div>
      <div class="bar" style="margin-top:4px">In-Person Workshop</div>
      <div style="margin-top:6px">
        <div class="price-row"><span class="label">Half-Day Workshop</span><span class="price">$18,000</span></div>
        <div class="price-row"><span class="label">Full-Day Workshop</span><span class="price">$26,000</span></div>
        <div class="price-row"><span class="label">Two-Day Intensive</span><span class="price">$45,000</span></div>
      </div>
      <p class="body" style="margin-top:10px">Workbooks, action plans and a 30-day follow-up call are part of every workshop.</p>
    </div>
    <div class="page light">
      <div class="bar">Virtual Workshop</div>
      <div style="margin-top:6px">
        <div class="price-row"><span class="label">90-Minute Session</span><span class="price">$7,500</span></div>
        <div class="price-row"><span class="label">Half-Day Online</span><span class="price">$12,000</span></div>
        <div class="price-row"><span class="label">Four-Week Program</span><span class="price">$28,000</span></div>
      </div>
      <div class="photo" role="img" aria-label="Team workshop in a meeting room" style="height:96px;margin-top:14px;background:linear-gradient(135deg,#cfcfcf,#5a5a5a)"></div>
      <span class="folio">19</span>
    </div>
  </section>

  <!-- Executive Coaching + Trusted By -->
  <section class="spread">
    <div class="page light">
      <div class="bar">Executive Coaching</div>
      <div style="margin-top:6px">
        <div class="price-row"><span class="label">Three-Month Program</span><span class="price">$15,000</span></div>
        <div class="price-row"><span class="label">Six-Month Program</span><span class="price">$27,000</span></div>
        <div class="price-row"><span class="label">Leadership Team Retainer</span><span class="price">$60,000</span></div>
      </div>
      <div class="card" style="margin-top:14px"><div class="label">What is included</div><div class="body">Bi-weekly calls, 360 review, goal scorecard and direct message access between sessions.</div></div>
    </div>
    <div class="page light">
      <div class="title">Trusted By <span class="accent">Leading</span> Organizations</div>
      <div class="rule"></div>
      <div class="grid2" style="margin-top:10px;grid-template-columns:1fr 1fr 1fr;gap:8px">
        <div class="logo-tile"></div><div class="logo-tile"></div><div class="logo-tile"></div>
        <div class="logo-tile"></div><div class="logo-tile"></div><div class="logo-tile"></div>
        <div class="logo-tile"></div><div class="logo-tile"></div><div class="logo-tile"></div>
        <div class="logo-tile"></div><div class="logo-tile"></div><div class="logo-tile"></div>
      </div>
      <div class="kicker" style="margin-top:16px">As featured in</div>
      <div class="grid2" style="margin-top:6px;grid-template-columns:1fr 1fr 1fr 1fr;gap:6px">
        <div class="logo-tile" style="height:18px"></div><div class="logo-tile" style="height:18px"></div><div class="logo-tile" style="height:18px"></div><div class="logo-tile" style="height:18px"></div>
      </div>
    </div>
  </section>

  <!-- Closing + Let's Create -->
  <section class="spread">
    <div class="page dark" style="display:flex;flex-direction:column;align-items:center;justify-content:center;text-align:center">
      <div class="kicker">Ready to grow your people?</div>
      <div class="mark" style="font-size:48px;margin-top:14px;color:var(--white)">QR7</div>
      <div style="font-size:6px;letter-spacing:2px;color:var(--grey);margin-top:2px">LUMEN</div>
      <div class="pill outline" style="margin-top:24px;font-size:6px;color:var(--soft)">www.QR7Lumen.com</div>
    </div>
    <div class="page light">
      <div class="title">Let’s Create Something <span class="accent">Unforgettable</span></div>
      <div class="rule"></div>
      <div class="list" style="margin-top:10px;gap:8px">
        <div class="row"><svg class="tick" viewBox="0 0 8 8"><path d="M1 4l2 2 4-4" stroke="#e1232b" stroke-width="1.4" fill="none"/></svg><div><div class="label">Discovery Call</div><div class="body">We learn your goals and audience.</div></div></div>
        <div class="row"><svg class="tick" viewBox="0 0 8 8"><path d="M1 4l2 2 4-4" stroke="#e1232b" stroke-width="1.4" fill="none"/></svg><div><div class="label">Customization</div><div class="body">Stories and tools shaped for you.</div></div></div>
        <div class="row"><svg class="tick" viewBox="0 0 8 8"><path d="M1 4l2 2 4-4" stroke="#e1232b" stroke-width="1.4" fill="none"/></svg><div><div class="label">Event Delivery</div><div class="body">A session your people remember.</div></div></div>
        <div class="row"><svg class="tick" viewBox="0 0 8 8"><path d="M1 4l2 2 4-4" stroke="#e1232b" stroke-width="1.4" fill="none"/></svg><div><div class="label">Follow-Up</div><div class="body">Resources to keep momentum going.</div></div></div>
      </div>
      <span class="folio">23</span>
    </div>
  </section>

  <!-- Contact -->
  <section class="spread">
    <div class="page dark">
      <div class="mark" style="font-size:56px;color:#262626;margin-top:20px">QR7</div>
      <div class="photo" role="img" aria-label="Speaker portrait in black and white" style="height:150px;margin-top:10px;background:linear-gradient(180deg,#4a4a4a,#0a0a0a)"></div>
    </div>
    <div class="page dark">
      <div class="title sm">Contact Information</div>
      <div class="rule"></div>
      <div class="list" style="margin-top:10px;gap:10px">
        <div class="row" style="align-items:center"><svg class="tick" viewBox="0 0 10 10" style="width:9px;height:9px"><path d="M2 1h2l1 2.5-1.3 1a6 6 0 0 0 2.8 2.8l1-1.3L10 7v2a1 1 0 0 1-1 1A8 8 0 0 1 1 2a1 1 0 0 1 1-1z" fill="#e1232b"/></svg><span class="body">(555) 014-2287</span></div>
        <div class="row" style="align-items:center"><svg class="tick" viewBox="0 0 10 10" style="width:9px;height:9px"><rect x="1" y="2" width="8" height="6" rx="1" fill="none" stroke="#e1232b"/><path d="M1 3l4 3 4-3" fill="none" stroke="#e1232b"/></svg><span class="body">booking@qr7lumen.com</span></div>
        <div class="row" style="align-items:center"><svg class="tick" viewBox="0 0 10 10" style="width:9px;height:9px"><circle cx="5" cy="5" r="4" fill="none" stroke="#e1232b"/><path d="M1 5h8M5 1c2 2 2 6 0 8M5 1c-2 2-2 6 0 8" fill="none" stroke="#e1232b" stroke-width=".7"/></svg><span class="body">www.QR7Lumen.com</span></div>
        <div class="row" style="align-items:center"><svg class="tick" viewBox="0 0 10 10" style="width:9px;height:9px"><path d="M5 9S1.5 5.5 1.5 3.5a3.5 3.5 0 0 1 7 0C8.5 5.5 5 9 5 9z" fill="#e1232b"/></svg><span class="body">Austin, Texas</span></div>
      </div>
      <div style="position:absolute;left:18px;right:18px;bottom:22px;display:flex;align-items:center;gap:6px;border-top:1px solid var(--edge);padding-top:8px">
        <span class="mark" style="font-size:11px">QR7</span><span class="body">Lumen · Speaking &amp; Leadership</span>
      </div>
    </div>
  </section>

</main>
</body>
</html>
```